Thankyou post card for our customers

we would like to have a design for a post card that we would like to send to our customers once they have hired from us to say thankyou and to offer them a discount on there next hire.

our business is called Wattlebrook Caravan Rentals.
we hire our camper trailers and are based in Australia so alot of our customers go to the outback bush, beach etc with our campers.
the post card dimesions are
Full Bleed Size

213 x 98 mm
2517 x 1158 pixels

Document Trim Size

210 x 95 mm
2481 x 1122 pixels

I want 4 lines for the name and address on the right have side of the post card (like normal post cards have

Requirements
Must have
• we want it to be double sided so a Design on front and back of post card
I have attached our logo and some other things we have used in previous business material up to you if you want to use what I have uploaded

please note the logo with sunset I have attached I do not want the round logo used just wanted to show you how great the sunset looks we have changed our logo to just be the Wattlebrook Caravan Rentals but wouldnt mind if you used a sunset like this on the whole of the card? but not limited to that.

front of card:
our logo on front page (which is just the Wattlebrook Caravan Rentals attachement WCR1)
and our details:
P: 0491 326 715
W: www.wattlebrookcaravanrentals.com.au
E:info@wattlebrookcaravanrentals.com.au

and the following to be on the front of the post card:

Dear Fellow Campers,
We hope you have arrived home safely, and are rested and relaxed from your trip away. It was our pleasure to have you hire one of our campers and would like to thankyou for your support, we trust you enjoyed glamping and would like to think you would hire from us again. to show our appreciation we would like to offer you a 20% discount on any minimum 7 day hire over the next 6 months. we look forward to hearing from you again soon.
sincerely,
Gareth & Colby

offer not valid in peak period or in conjuction with any other offer

Full Bleed Size

213 x 98 mm
2517 x 1158 pixels

Document Trim Size

210 x 95 mm
2481 x 1122 pixels

Back of Card:

I want "Thankyou" written at top and then how ever else you design it

```html
<!DOCTYPE html>
<html lang="en">
<head>
<meta charset="utf-8">
<title>Wattlebrook Caravan Rentals – Thank You Postcard</title>
<link rel="stylesheet" href="https://fonts.googleapis.com/css2?family=Open+Sans:ital,wght@0,400;0,600;0,700;1,400&display=swap">
<style>
  :root {
    --page-bg: #e9e9e9;
    --card-black: #050505;
    --brand-orange: #c8702a;
    --brand-ink: #1b222c;
    --body-ink: #222a33;
    --sky-top: #2f63a8;
    --sky-mid: #86a8d2;
    --horizon: #e6eaee;
    --sand-light: #eadbc4;
    --sand-deep: #d3ab7e;
    --address-line: #4a4a4a;
    --card-shadow: rgba(0, 0, 0, 0.28);
  }

  * { margin: 0; padding: 0; box-sizing: border-box; }

  html, body {
    width: 1200px;
    height: 900px;
    overflow: hidden;
  }

  body {
    background: var(--page-bg);
    font-family: "Open Sans", Arial, sans-serif;
    display: flex;
    flex-direction: column;
    align-items: center;
    justify-content: center;
    gap: 34px;
  }

  .postcard {
    position: relative;
    width: 880px;
    height: 400px;
    overflow: hidden;
    box-shadow: 0 6px 18px var(--card-shadow);
  }

  .brand-name {
    text-transform: uppercase;
    line-height: 1;
    white-space: nowrap;
  }

  .brand-name__main,
  .brand-name__sub { display: block; }

  /* ---------- Back: black with thank you + brand ---------- */
  .postcard--back { background: var(--card-black); }

  .thankyou-heading {
    position: absolute;
    top: 46px;
    left: 0;
    right: 0;
    text-align: center;
    color: var(--brand-orange);
    font-size: 34px;
    font-weight: 600;
    letter-spacing: 6px;
    text-transform: uppercase;
  }

  .postcard--back .brand-name {
    position: absolute;
    left: 0;
    right: 0;
    top: 148px;
    text-align: center;
    color: var(--brand-orange);
    font-weight: 600;
  }

  .postcard--back .brand-name__main {
    font-size: 80px;
    letter-spacing: 1px;
  }

  .postcard--back .brand-name__sub {
    font-size: 38px;
    margin-top: 12px;
  }

  /* ---------- Front: scene, message, contacts, address ---------- */
  .postcard--front .scene-photo {
    position: absolute;
    inset: 0;
    background:
      linear-gradient(100deg, rgba(255,255,255,0) 45%, rgba(240,238,235,0.7) 70%, rgba(245,243,240,0.9) 100%),
      linear-gradient(180deg,
        var(--sky-top) 0%,
        var(--sky-mid) 26%,
        var(--horizon) 44%,
        var(--sand-light) 52%,
        var(--sand-deep) 82%,
        var(--sand-light) 100%);
  }

  .postcard--front .brand-name {
    position: absolute;
    left: 50px;
    top: 36px;
    color: var(--brand-ink);
    font-weight: 700;
  }

  .postcard--front .brand-name__main {
    font-size: 44px;
    letter-spacing: 0.5px;
  }

  .postcard--front .brand-name__sub {
    font-size: 19.5px;
    margin-top: 6px;
    margin-left: 2px;
  }

  .contact-details {
    position: absolute;
    right: 50px;
    top: 40px;
    list-style: none;
    text-align: right;
    color: var(--brand-ink);
    font-size: 12px;
    font-weight: 600;
    line-height: 1.6;
  }

  .contact-details__label {
    color: var(--brand-orange);
    font-weight: 700;
    margin-right: 4px;
  }

  .thankyou-message {
    position: absolute;
    left: 52px;
    top: 124px;
    width: 410px;
    color: var(--body-ink);
    font-size: 11.5px;
    line-height: 1.5;
  }

  .thankyou-message__greeting {
    font-weight: 700;
    margin-bottom: 4px;
  }

  .thankyou-message__offer { font-weight: 700; }

  .thankyou-message__signoff {
    margin-top: 6px;
    font-weight: 600;
  }

  .offer-terms {
    position: absolute;
    left: 52px;
    bottom: 16px;
    color: var(--body-ink);
    font-size: 9.5px;
    font-style: italic;
  }

  .address-lines {
    position: absolute;
    left: 500px;
    top: 180px;
    width: 330px;
    height: 160px;
  }
</style>
</head>
<body>

  <section class="postcard postcard--back" aria-label="Postcard back">
    <p class="thankyou-heading">Thankyou</p>
    <h1 class="brand-name">
      <span class="brand-name__main">Wattlebrook</span>
      <span class="brand-name__sub">Caravan Rentals</span>
    </h1>
  </section>

  <section class="postcard postcard--front" aria-label="Postcard front">
    <div class="scene-photo" role="img"
         aria-label="Photograph of a camper trailer driving away across outback sand dunes under a blue sky, leaving curved tyre tracks in the sand"></div>

    <h2 class="brand-name">
      <span class="brand-name__main">Wattlebrook</span>
      <span class="brand-name__sub">Caravan Rentals</span>
    </h2>

    <ul class="contact-details">
      <li><span class="contact-details__label">P:</span>0491 326 715</li>
      <li><span class="contact-details__label">W:</span>www.wattlebrookcaravanrentals.com.au</li>
      <li><span class="contact-details__label">E:</span>info@wattlebrookcaravanrentals.com.au</li>
    </ul>

    <div class="thankyou-message">
      <p class="thankyou-message__greeting">Dear Fellow Campers,</p>
      <p>We hope you have arrived home safely, and are rested and relaxed from your trip away. It was our pleasure to have you hire one of our campers and we would like to thank you for your support. We trust you enjoyed glamping and would like to think you would hire from us again. To show our appreciation we would like to offer you a <span class="thankyou-message__offer">20% discount on any minimum 7 day hire</span> over the next 6 months. We look forward to hearing from you again soon.</p>
      <p class="thankyou-message__signoff">Sincerely,<br>Gareth &amp; Colby</p>
    </div>

    <p class="offer-terms">Offer not valid in peak period or in conjunction with any other offer.</p>

    <svg class="address-lines" viewBox="0 0 330 160" aria-label="Name and address lines">
      <g stroke="var(--address-line)" stroke-width="1.2">
        <line x1="0" y1="10" x2="330" y2="10"/>
        <line x1="0" y1="52" x2="330" y2="52"/>
        <line x1="0" y1="94" x2="330" y2="94"/>
        <line x1="0" y1="136" x2="330" y2="136"/>
      </g>
    </svg>
  </section>

</body>
</html>
```